Brett Olsen Building Business Card Design

Hi,

I need a business card for my Building company.
I am a Builder and build homes for clients.
I am looking for a sophisticated logo that can be used on business cards, envelopes and letter heads.
I am trying to take my business to the next level and need a professional business card.

Colours: Please use white, black, dark grey and bright blue.

Thank you,

Carol and Brett.

Target Market(s)

1. Home and Building Companies 2. Potential customers

Industry/Entity Type

Business

Contact Information for Business Card

Brett Olsen Building PTY LTD

Brett Olsen

Director

A.B.N. 37 829 516 073

BUILDERS LICENCE No. 573019k

Mobile: 0412 907 381

Email: brettolsenbuilding@mailvane.com.au

Requirements
Must have
• The following is compulsory to have in the designs:

Brett Olsen Building PTY LTD (business name)

Brett Olsen (contact name)

Director (position)

A.B.N. 37 829 516 073

Builders Licence No. 573019k

Mobile: 0412 907 381

Nice to have
• Logo for business
Should not have
• Should not be cluttered.

I am looking for a clean, sophisticated and professional business card design.

```html
<!DOCTYPE html>
<html lang="en">
<head>
<meta charset="utf-8">
<title>Brett Olsen Building – Business Card</title>
<link rel="stylesheet" href="https://fonts.googleapis.com/css2?family=Montserrat:wght@600;700&family=Mulish:wght@400;500&display=swap">
<style>
  :root {
    --page: #ffffff;
    --blue: #0a95d3;
    --blue-deep: #0a86c6;
    --blue-light: #e9f7ff;
    --charcoal: #3a3a3c;
    --band: #3b3b3d;
    --ink: #111111;
    --white: #ffffff;
    --mark-grey: #a7a9ac;
    --shadow: rgba(0, 0, 0, 0.45);
  }
  * { margin: 0; padding: 0; box-sizing: border-box; }
  html, body {
    width: 1200px; height: 900px; overflow: hidden;
    background: var(--page);
  }
  .canvas { position: relative; width: 1200px; height: 900px; }

  .card {
    position: absolute; width: 554px; height: 311px; overflow: hidden;
    box-shadow: 10px 12px 14px var(--shadow);
  }

  /* Front */
  .card--front {
    left: 88px; top: 124px;
    background: radial-gradient(ellipse 300px 200px at 52% 33%, var(--blue-light) 0%, #7fd0f2 30%, var(--blue) 70%, var(--blue-deep) 100%);
  }
  .front__name {
    position: absolute; left: 0; right: 0; top: 96px;
    text-align: center;
    font-family: "Montserrat", sans-serif; font-weight: 700;
    font-size: 38px; line-height: 1.1; letter-spacing: 1px;
    text-transform: uppercase; color: var(--ink);
  }
  .front__band {
    position: absolute; left: 0; right: 0; top: 244px; height: 43px;
    background: var(--band);
    display: flex; align-items: center; justify-content: center; gap: 7px;
    color: var(--white); font-family: "Montserrat", sans-serif; font-weight: 600;
  }
  .front__company { font-size: 23px; letter-spacing: 0.5px; }
  .front__suffix { font-size: 11px; letter-spacing: 1px; padding-top: 7px; }

  /* Back */
  .card--back { left: 535px; top: 470px; background: var(--charcoal); }
  .back__stripe { position: absolute; left: 135px; top: 24px; width: 419px; height: 44px; }
  .back__mark {
    position: absolute; left: 30px; top: 40px; width: 160px;
    display: flex; align-items: center; gap: 10px;
    font-family: "Montserrat", sans-serif; font-weight: 700;
    font-size: 20px; line-height: 1.15; text-transform: uppercase; color: var(--white);
  }
  .back__mark-square { width: 14px; height: 14px; background: var(--white); flex: none; }
  .back__person {
    position: absolute; right: 43px; top: 31px;
    font-family: "Montserrat", sans-serif; font-weight: 600;
    font-size: 23px; letter-spacing: 0.5px; color: var(--white);
  }
  .back__role {
    position: absolute; right: 43px; top: 80px;
    font-family: "Mulish", sans-serif; font-size: 20px; color: var(--blue);
  }
  .contact {
    position: absolute; right: 40px; display: flex; align-items: center; gap: 16px;
    font-family: "Mulish", sans-serif; font-size: 16px; color: var(--white);
  }
  .contact--phone { top: 128px; }
  .contact--email { top: 180px; }
  .contact__at { color: var(--blue); }
  .back__legal {
    position: absolute; left: 47px; top: 246px; display: flex; gap: 32px;
    font-family: "Mulish", sans-serif; font-size: 15.5px; color: var(--white);
  }

  /* Standalone mark */
  .mark-standalone {
    position: absolute; left: 55px; top: 770px; width: 200px;
    font-family: "Montserrat", sans-serif; font-weight: 700;
    font-size: 26px; line-height: 1.1; text-transform: uppercase; color: var(--mark-grey);
  }
</style>
</head>
<body>
<main class="canvas">

  <section class="card card--front" aria-label="Business card front">
    <p class="front__name">Brett Olsen<br>Building</p>
    <div class="front__band">
      <span class="front__company">BRETT OLSEN BUILDING</span>
      <span class="front__suffix">PTY LTD</span>
    </div>
  </section>

  <section class="card card--back" aria-label="Business card back">
    <svg class="back__stripe" viewBox="0 0 419 44" aria-hidden="true">
      <polygon points="0,0 419,0 419,44 46,44" fill="var(--blue)"/>
    </svg>
    <div class="back__mark"><span class="back__mark-square"></span><span>Brett Olsen Building</span></div>
    <h1 class="back__person">BRETT OLSEN</h1>
    <p class="back__role">Director</p>

    <p class="contact contact--phone">
      <span>0412 907 381</span>
      <svg width="22" height="38" viewBox="0 0 22 38" aria-hidden="true">
        <rect x="15" y="0" width="3" height="8" fill="var(--blue)"/>
        <rect x="1" y="6" width="20" height="32" rx="3" fill="var(--blue)"/>
        <rect x="4" y="10" width="14" height="9" fill="var(--charcoal)"/>
        <g fill="var(--charcoal)">
          <rect x="4" y="22" width="3" height="3"/><rect x="9.5" y="22" width="3" height="3"/><rect x="15" y="22" width="3" height="3"/>
          <rect x="4" y="27" width="3" height="3"/><rect x="9.5" y="27" width="3" height="3"/><rect x="15" y="27" width="3" height="3"/>
          <rect x="4" y="32" width="3" height="3"/><rect x="9.5" y="32" width="3" height="3"/><rect x="15" y="32" width="3" height="3"/>
        </g>
      </svg>
    </p>

    <p class="contact contact--email">
      <span>brettolsenbuilding<span class="contact__at">@</span>mailvane.com.au</span>
      <svg width="35" height="25" viewBox="0 0 35 25" aria-hidden="true">
        <rect width="35" height="25" fill="var(--blue)"/>
        <polyline points="1,1 17.5,14 34,1" fill="none" stroke="var(--charcoal)" stroke-width="2"/>
        <line x1="1" y1="24" x2="13" y2="11" stroke="var(--charcoal)" stroke-width="2"/>
        <line x1="34" y1="24" x2="22" y2="11" stroke="var(--charcoal)" stroke-width="2"/>
      </svg>
    </p>

    <p class="back__legal">
      <span>A.B.N. 37 829 516 073</span>
      <span>BUILDERS LICENCE No. 573019k</span>
    </p>
  </section>

  <p class="mark-standalone">Brett Olsen Building</p>

</main>
</body>
</html>
```